WP website design (Vorne)

We need a wordpress design for an established auction and real estate company based in Kentucky. The winning design will incorporate a professional color scheme with company logo in a clean layout with specified widgets. The design needs to consider that this will be developed on a responsive theme. Colors will complement the colors in the logo.

Industry/Entity Type

Real Estate

Font styles to use
Sans Serif

Requirements
Must have
• - Navigation:
1) Home 2) Auctions 3) Real Estate Listings 4) Our Services 5) Why Auctions 6) About Us 7) Past Auctions 8) Contact Us

Homeage will have slideshow, please use stock real estate image as the initial slide. Homepage will have this content: "Martin Vorne Auctioneer Real Estate Broker

Buying or selling you can count on Martin Vorne Auctioneer to deliver a quality auction experience. We handle all the details from initial handshake to final payment. We are with you every step of the way giving our sellers the service and results they deserve. You only have one chance for a successful auction. Contact us today to see how our experience and know-how can work for you. We are confident that you will appreciate our higher standard of service."

Footer will have smaller company logo, and attached association logos and this contact info:
Phone: (270) 555-0148
Contacts: Martin Vorne
Email: martinvorne@mailbrook.example
Address: 482 Pellworth Lane • Bowling Green, KY 42917

Widgets:
1) email sign up 2) Social media (twitter, Youtube - can also be in header 3) News & Events Blog widget 4) testimonials blog 5) Featured Video widget
Nice to have
• Nice to Have:
- demonstrate the drop-down menu styling, e.g. under Auctions
-Upcoming Auctions
-Online Auctions
-Past Auctions

```html
<!DOCTYPE html>
<html lang="en">
<head>
<meta charset="utf-8">
<title>Martin Vorne Auctioneer Real Estate Broker</title>
<link href="https://fonts.googleapis.com/css2?family=Open+Sans:wght@400;600;700&display=swap" rel="stylesheet">
<style>
:root{
  --blue:#1b5fab;
  --blue-dark:#134a87;
  --yellow:#f4b400;
  --grey:#6d6e70;
  --grey-dark:#4a4a4a;
  --text:#555;
  --light:#f2f2f2;
  --line:#dcdcdc;
  --white:#fff;
  --red:#c4302b;
}
*{box-sizing:border-box;margin:0;padding:0}
html,body{width:1200px;height:2380px;overflow:hidden}
body{font-family:"Open Sans",Arial,sans-serif;color:var(--text);background:var(--white);position:relative}
.wrap{width:1040px;margin:0 auto;position:relative}

/* header */
.site-header{height:128px;position:relative}
.brand{position:absolute;left:0;top:18px;display:flex;align-items:center;gap:12px}
.brand-mark{width:56px;height:56px;background:var(--blue);border-radius:50%}
.brand-name{font-size:40px;font-weight:700;color:var(--blue)}
.header-tools{position:absolute;right:0;top:18px;display:flex;align-items:center;gap:10px}
.social-dot{width:26px;height:26px;background:var(--blue);border-radius:3px}
.social-dot.red{background:var(--red)}
.btn-sm{height:28px;padding:0 20px;line-height:28px;font-size:13px;color:var(--white);background:var(--blue);border-radius:2px}
.btn-sm.yellow{background:var(--yellow)}
.search{position:absolute;right:0;top:66px;width:200px;height:30px;border:1px solid var(--line);font-size:12px;color:#aaa;line-height:28px;padding-left:10px}
.search::after{content:"";position:absolute;right:0;top:0;width:30px;height:28px;background:var(--yellow)}

.main-nav{height:34px;background:var(--blue);position:relative;z-index:5}
.main-nav ul{list-style:none;display:flex;width:1040px;margin:0 auto}
.main-nav li{position:relative;font-size:13px;color:var(--white);line-height:34px;padding:0 24px}
.main-nav li.active{background:var(--yellow)}
.dropdown{position:absolute;left:0;top:34px;width:170px;background:var(--yellow);padding:6px 0}
.dropdown span{display:block;background:var(--white);color:var(--grey-dark);font-size:12px;line-height:26px;margin:4px 8px;padding-left:10px}

/* hero */
.hero{height:520px;background:linear-gradient(160deg,#c9dcec 0%,#a7c3d9 45%,#6f8f5a 75%,#4f6d3c 100%);position:relative}
.hero-caption{position:absolute;left:0;right:0;bottom:54px;height:56px;background:rgba(40,40,40,.7);text-align:center;line-height:56px;font-size:26px;color:var(--white)}
.hero-arrow{position:absolute;top:240px;width:28px;height:40px;background:rgba(255,255,255,.7)}
.hero-arrow.l{left:0}.hero-arrow.r{right:0}
.dots{position:absolute;bottom:18px;left:0;right:0;display:flex;justify-content:center;gap:6px}
.dots i{width:9px;height:9px;border-radius:50%;background:#ccc}
.dots i.on{background:var(--blue)}

/* sections */
.section-title{font-size:18px;font-weight:700;color:var(--blue);text-transform:uppercase;margin-bottom:4px}
.rule{height:2px;background:var(--line);margin-bottom:16px}
.about{margin-top:40px;display:flex;gap:40px}
.about-body{flex:1}
.about-row{display:flex;gap:16px;align-items:flex-start}
.avatar{width:100px;height:100px;border-radius:50%;background:linear-gradient(#e3c6a8,#b89478);flex:none}
.about p{font-size:14px;line-height:22px;font-style:italic}
.about p+p{margin-top:12px}
.video{width:340px;height:220px;background:linear-gradient(#b8cde0,#8aa267);position:relative;border:4px solid var(--light)}
.play{position:absolute;left:142px;top:82px;width:48px;height:40px;background:var(--red);border-radius:8px}
.play::after{content:"";position:absolute;left:19px;top:11px;border-left:14px solid var(--white);border-top:9px solid transparent;border-bottom:9px solid transparent}

.listings{margin-top:50px;display:flex;gap:40px}
.cards{width:700px;display:grid;grid-template-columns:1fr 1fr;gap:30px 20px}
.card{border:1px solid var(--line);background:var(--white)}
.card-photo{height:170px;background:linear-gradient(#bcd3e8,#9cae7c 70%,#7b8e5e)}
.card-photo.b{background:linear-gradient(#c7d8e6,#a89a86 60%,#84906a)}
.card-body{padding:12px 14px}
.card h3{font-size:18px;font-weight:600;color:var(--grey-dark);text-align:center;margin-bottom:6px}
.card p{font-size:12px;line-height:18px;text-align:center}
.card-meta{display:flex;justify-content:space-between;font-size:11px;line-height:15px;border-top:1px solid var(--line);padding:8px 14px;align-items:center}
.card-meta span{display:flex;align-items:center;gap:6px}
.card-actions{display:flex}
.card-actions span{flex:1;background:var(--grey);color:var(--white);font-size:11px;text-align:center;line-height:28px;border-right:1px solid var(--white)}
.card-actions span:last-child{border:0}

.sidebar{flex:1}
.widget{border:1px solid var(--line);margin-bottom:26px}
.widget-head{display:flex;align-items:center;gap:10px;padding:8px 12px;border-bottom:1px solid var(--line);font-size:16px;font-weight:600;color:var(--grey-dark)}
.widget-head i{width:24px;height:24px;background:var(--blue);border-radius:3px}
.news-item{display:flex;gap:10px;padding:12px}
.news-thumb{width:60px;height:46px;background:linear-gradient(#b9cde1,#8a9e6e);flex:none}
.news-item b{display:block;font-size:12px;color:var(--blue)}
.news-item small{font-size:10px;line-height:14px;display:block}
.more{text-align:right;font-size:10px;color:var(--blue);padding:0 12px 10px}
.signup{background:var(--blue);color:var(--white);padding:14px 16px;margin-bottom:30px}
.signup h4{font-size:17px;text-align:center;font-weight:600}
.signup p{font-size:10px;text-align:center;margin:4px 0 10px}
.signup-row{display:flex}
.signup-row span{flex:1;height:26px;background:var(--white)}
.signup-row b{width:70px;background:var(--yellow);font-size:11px;line-height:26px;text-align:center}
.testi-head{display:flex;justify-content:space-between;align-items:center}
.testi-head .section-title{color:var(--grey-dark)}
.arrows{display:flex;gap:4px}
.arrows i{width:20px;height:20px;border-radius:50%;background:var(--grey)}
.arrows i.on{background:var(--blue)}
.testi{display:flex;gap:12px;margin-bottom:22px;align-items:flex-start}
.testi-who{width:60px;text-align:center;font-size:9px;flex:none}
.testi-who i{display:block;width:46px;height:46px;margin:0 auto 4px;border-radius:50%;background:linear-gradient(#e2c4a6,#b38c70)}
.bubble{background:var(--grey);color:var(--white);font-size:10px;line-height:15px;padding:10px 12px;border-radius:4px}

.pager{display:flex;justify-content:center;gap:6px;margin-top:40px}
.pager i{width:26px;height:26px;border-radius:50%;background:#ccc}
.pager i.on{background:var(--blue)}

/* footer */
.site-footer{position:absolute;left:0;right:0;top:1900px;height:440px;background:var(--light);border-top:3px solid var(--blue)}
.foot-cols{display:flex;gap:40px;padding-top:30px}
.foot-col{width:230px}
.foot-col h5{font-size:14px;font-weight:700;color:var(--grey-dark);text-transform:uppercase;margin-bottom:6px}
.foot-col .rule{margin-bottom:10px}
.foot-col li{list-style:none;font-size:12px;line-height:22px;display:flex;gap:8px;align-items:center}
.foot-col li.hl{color:var(--blue)}
.ico{width:16px;height:16px;background:var(--blue);border-radius:2px;flex:none;display:flex;align-items:center;justify-content:center}
.ico.red{background:var(--red)}
.badges{flex:1;display:grid;grid-template-columns:repeat(3,1fr);gap:16px;padding-top:20px}
.badges i{height:40px;background:#333;border-radius:4px}
.badges i.sq{width:40px;justify-self:center}
.foot-brand{display:flex;align-items:center;gap:8px;margin-top:30px;justify-content:flex-end}
.foot-brand i{width:26px;height:26px;border-radius:50%;background:var(--blue)}
.foot-brand span{font-size:20px;font-weight:700;color:var(--blue)}
.bottom-bar{position:absolute;left:0;right:0;top:2340px;height:40px;background:var(--blue);color:var(--white);font-size:11px;line-height:40px}
</style>
</head>
<body>

<header class="site-header wrap">
  <div class="brand"><span class="brand-mark"></span><span class="brand-name">Vorne</span></div>
  <div class="header-tools">
    <span class="social-dot" aria-label="Social link"></span>
    <span class="social-dot red" aria-label="Video channel link"></span>
    <span class="btn-sm">Sign In</span>
    <span class="btn-sm yellow">Sign Up</span>
  </div>
  <div class="search">Search here</div>
</header>

<nav class="main-nav">
  <ul>
    <li>Home</li>
    <li class="active">Auctions
      <div class="dropdown"><span>Upcoming Auctions</span><span>Online Auctions</span><span>Past Auctions</span></div>
    </li>
    <li>Real Estate Listings</li>
    <li>Our Services</li>
    <li>Why Auctions</li>
    <li>About Us</li>
    <li>Past Auctions</li>
    <li>Contact Us</li>
  </ul>
</nav>

<section class="hero" role="img" aria-label="Couple looking at a house with a sold sign">
  <span class="hero-arrow l"></span><span class="hero-arrow r"></span>
  <div class="hero-caption">Martin Vorne Auctioneer Real Estate Broker</div>
  <div class="dots"><i class="on"></i><i></i><i></i></div>
</section>

<main class="wrap">
  <section class="about">
    <div class="about-body">
      <h2 class="section-title">About Us</h2>
      <div class="rule"></div>
      <div class="about-row">
        <div class="avatar" role="img" aria-label="Smiling agent portrait"></div>
        <div>
          <p>Buying or selling you can count on Martin Vorne Auctioneer to deliver a quality auction experience. We handle all the details from initial handshake to final payment. We are with you every step of the way giving our sellers the service and results they deserve. You only have one chance for a successful auction.</p>
        </div>
      </div>
      <p>Contact us today to see how our experience and know-how can work for you. We are confident that you will appreciate our higher standard of service.</p>
    </div>
    <div class="video" role="img" aria-label="Featured video of a brick home"><span class="play"></span></div>
  </section>

  <section class="listings">
    <div>
      <h2 class="section-title">Latest Auctions</h2>
      <div class="rule"></div>
      <div class="cards">
        <article class="card">
          <div class="card-photo" role="img" aria-label="Two-storey brick home"></div>
          <div class="card-body"><h3>Lorem ipsum dolor sit</h3><p>Nam at nunc in imperdiet massa. Aliquam eleifend facilisis nisi non ornare. Curabitur in egestas turpis.</p></div>
          <div class="card-meta"><span><svg width="10" height="14" viewBox="0 0 10 14"><path d="M5 0a5 5 0 0 1 5 5c0 4-5 9-5 9S0 9 0 5a5 5 0 0 1 5-5z" fill="#6d6e70"/></svg>Location</span><span>P.O. Box 50917<br>Glenhaven, KY 42990</span></div>
          <div class="card-actions"><span>Auction Date</span><span>Auction Find</span><span>BID NOW</span></div>
        </article>
        <article class="card">
          <div class="card-photo b" role="img" aria-label="Suburban family house"></div>
          <div class="card-body"><h3>Ipsum dolor sit</h3><p>Nam at nunc in imperdiet massa. Aliquam eleifend facilisis nisi non ornare. Curabitur in egestas turpis.</p></div>
          <div class="card-meta"><span><svg width="10" height="14" viewBox="0 0 10 14"><path d="M5 0a5 5 0 0 1 5 5c0 4-5 9-5 9S0 9 0 5a5 5 0 0 1 5-5z" fill="#6d6e70"/></svg>Location</span><span>P.O. Box 50917<br>Glenhaven, KY 42990</span></div>
          <div class="card-actions"><span>Auction Date</span><span>Auction Find</span><span>BID NOW</span></div>
        </article>
        <article class="card">
          <div class="card-photo b" role="img" aria-label="Stone front home with lawn"></div>
          <div class="card-body"><h3>Lorem ipsum dolor sit</h3><p>Nam at nunc in imperdiet massa. Aliquam eleifend facilisis nisi non ornare. Curabitur in egestas turpis.</p></div>
          <div class="card-meta"><span><svg width="10" height="14" viewBox="0 0 10 14"><path d="M5 0a5 5 0 0 1 5 5c0 4-5 9-5 9S0 9 0 5a5 5 0 0 1 5-5z" fill="#6d6e70"/></svg>Location</span><span>P.O. Box 50917<br>Glenhaven, KY 42990</span></div>
          <div class="card-actions"><span>Auction Date</span><span>Auction Find</span><span>BID NOW</span></div>
        </article>
        <article class="card">
          <div class="card-photo" role="img" aria-label="Grey two-storey house"></div>
          <div class="card-body"><h3>Ipsum dolor sit</h3><p>Nam at nunc in imperdiet massa. Aliquam eleifend facilisis nisi non ornare. Curabitur in egestas turpis.</p></div>
          <div class="card-meta"><span><svg width="10" height="14" viewBox="0 0 10 14"><path d="M5 0a5 5 0 0 1 5 5c0 4-5 9-5 9S0 9 0 5a5 5 0 0 1 5-5z" fill="#6d6e70"/></svg>Location</span><span>P.O. Box 50917<br>Glenhaven, KY 42990</span></div>
          <div class="card-actions"><span>Auction Date</span><span>Auction Find</span><span>BID NOW</span></div>
        </article>
      </div>
    </div>

    <aside class="sidebar">
      <div class="widget">
        <div class="widget-head"><i></i>News And Events</div>
        <div class="news-item"><div class="news-thumb" role="img" aria-label="News house photo"></div><div><b>Lorem ipsum dolor</b><small>Nam at nunc in imperdiet massa, aliquam eleifend facilisis nisi non ornare tempor.</small></div></div>
        <div class="more">View All</div>
      </div>
      <div class="signup">
        <h4>Email Sign Up</h4>
        <p>Get our latest auction news and listings sent to your inbox.</p>
        <div class="signup-row"><span></span><b>Submit</b></div>
      </div>
      <div class="testi-head"><h2 class="section-title">Testimonials</h2><div class="arrows"><i></i><i class="on"></i></div></div>
      <div class="rule"></div>
      <div class="testi"><div class="testi-who"><i role="img" aria-label="Client portrait"></i>Client Name</div><div class="bubble">Pleasure to work with. They handled every detail and got us a great result at our auction.</div></div>
      <div class="testi"><div class="testi-who"><i role="img" aria-label="Client portrait"></i>Client Name</div><div class="bubble">Pleasure to work with. They handled every detail and got us a great result at our auction.</div></div>
      <div class="testi"><div class="testi-who"><i role="img" aria-label="Client portrait"></i>Client Name</div><div class="bubble">Pleasure to work with. They handled every detail and got us a great result at our auction.</div></div>
    </aside>
  </section>

  <div class="pager"><i></i><i class="on"></i></div>
</main>

<footer class="site-footer">
  <div class="wrap">
    <div class="foot-cols">
      <div class="foot-col">
        <h5>In Brief</h5><div class="rule"></div>
        <ul><li class="hl">About us</li><li>Current auctions</li><li>Becoming a property seller</li></ul>
      </div>
      <div class="foot-col">
        <h5>Contact</h5><div class="rule"></div>
        <ul>
          <li><span class="ico"><svg width="8" height="11" viewBox="0 0 10 14"><path d="M5 0a5 5 0 0 1 5 5c0 4-5 9-5 9S0 9 0 5a5 5 0 0 1 5-5z" fill="#fff"/></svg></span>482 Pellworth Lane • Bowling Green, KY 42917</li>
          <li><span class="ico"><svg width="10" height="10" viewBox="0 0 10 10"><path d="M2 0l2 2-1 2c1 1 2 2 3 3l2-1 2 2-2 2C4 10 0 6 0 2z" fill="#fff"/></svg></span>(270) 555-0148</li>
          <li><span class="ico"><svg width="10" height="8" viewBox="0 0 10 8"><rect width="10" height="8" fill="#fff"/><path d="M0 0l5 4 5-4" stroke="#1b5fab" fill="none"/></svg></span>martinvorne@mailbrook.example</li>
          <li><span class="ico"><svg width="8" height="8" viewBox="0 0 8 8"><circle cx="4" cy="2" r="2" fill="#fff"/><rect x="0" y="5" width="8" height="3" fill="#fff"/></svg></span>Martin Vorne</li>
        </ul>
      </div>
      <div class="foot-col">
        <h5>Staying in Touch</h5><div class="rule"></div>
        <ul><li><span class="ico red"></span>Video channel</li><li><span class="ico"></span>Social feed</li></ul>
      </div>
      <div class="badges">
        <i></i><i></i><i></i><i></i><i></i><i class="sq"></i>
      </div>
    </div>
    <div class="foot-brand"><i></i><span>Vorne</span></div>
  </div>
</footer>
<div class="bottom-bar"><div class="wrap">Copyright © Martin Vorne. All rights reserved.</div></div>

</body>
</html>
```